PIP Post Card

Our firm name is Milo T. Varnum Attorneys at Law. We exclusively handle personal injury and PIP arbitration cases.We are experienced aggressive and determined, attorneys. We are result and relationship driven. We would like to be the premier law firm in our new area of Red Bank (Central New Jersey). We represent people who have been injured in accidents (motor vehicle, slip and fall, wrongful death, medical malpractice, nursing home injuries, workers comp,and premise and product liability) and the medical providers who treat them.

We will need a post card to mail to medical providers. The biggest portion of our business is that we represent doctors who have treated injured parties. This is called "No-Fault Personal Injury Protection Arbitration". What we do is file a law suit against the car insurance company to pay for medical bills that they have denied or gone unpaid. We have collected over millions of dollars for medical providers.

This post card will need to pass a "gate keeper" as most doctors do not sort their own mail. This card needs to stand out. On the post card we will need our signature logo, which is attached on the letterhead provided. To get more ideas about our firm please check out our website at milovarnum.com .We would like to see a design that uses our colors of dark and medium blue.

```html
<!DOCTYPE html>
<html lang="en">
<head>
<meta charset="utf-8">
<title>Milo T. Varnum, P.A. – PIP Postcard</title>
<link rel="stylesheet" href="https://fonts.googleapis.com/css2?family=Oswald:wght@500;700&family=Tinos:wght@400;700&family=Lato:wght@700&display=swap">
<style>
:root{
  --navy:#15294a;
  --navy-deep:#0f1f3a;
  --blue:#1f6bb5;
  --blue-light:#2f82cf;
  --white:#ffffff;
  --paper:#f4f6f9;
  --stage:#e6e8ec;
  --ink:#1d2535;
  --line:#9aa3ad;
}
*{box-sizing:border-box;margin:0;padding:0}
html,body{width:898px;height:1200px;overflow:hidden;background:var(--stage)}
body{position:relative;font-family:"Tinos",serif;color:var(--ink)}
.card{position:absolute;left:62px;width:776px;background:var(--white);overflow:hidden;box-shadow:0 4px 14px rgba(0,0,0,.18)}
.front{top:42px;height:513px}
.back{top:615px;height:503px}
.abs{position:absolute}

/* shared marks */
.firm-mark{display:flex;align-items:center;gap:10px;color:var(--navy)}
.firm-mark .square{width:46px;height:46px;background:var(--blue)}
.firm-mark .name{font-family:"Tinos",serif;font-weight:400;font-size:25px;line-height:1}
.firm-mark .sub{font-family:"Tinos",serif;font-weight:400;font-size:12px;letter-spacing:.5px;text-align:right;margin-top:2px}
.icon{display:inline-block;vertical-align:middle}

/* front */
.front .top-swoosh{top:0;left:0;width:776px;height:160px}
.front .logo{left:78px;top:42px}
.phone-tab{display:flex;align-items:center;gap:10px;color:var(--white);font-family:"Lato",sans-serif;font-weight:700;font-size:23px;padding-left:36px;height:44px}
.phone-tab.primary{left:506px;top:13px;width:270px;background:var(--blue);border-radius:14px 0 0 14px}
.phone-tab.secondary{left:506px;top:66px;width:270px;background:var(--navy);border-radius:22px 0 0 0;height:48px}
.lead-panel{left:0;top:118px;width:270px;height:395px;background:var(--blue)}
.headline{left:24px;top:152px;width:230px;font-family:"Oswald",sans-serif;font-weight:700;font-size:23px;line-height:30px;color:var(--white);text-transform:uppercase}
.lead-copy{left:104px;top:276px;width:160px;font-size:15.5px;line-height:18px;color:var(--white)}
.portrait{left:-6px;top:278px;width:130px;height:235px;background:linear-gradient(180deg,#5d6f86,#1b2433);border-radius:60px 60px 0 0}
.feature-panel{left:256px;top:118px;width:520px;height:296px;background:var(--navy)}
.feature-panel .frame{position:absolute;top:28px;width:228px;height:118px;border:5px solid var(--blue-light);border-radius:10px}
.feature-panel .frame.crash{left:30px;background:linear-gradient(135deg,#6b7480,#a34a4a 60%,#3b3f46)}
.feature-panel .frame.surgery{left:278px;background:linear-gradient(135deg,#8fc6d8,#4d8fb4 55%,#d9e6ee)}
.feature-title{position:absolute;left:24px;top:178px;width:480px;white-space:nowrap;font-family:"Oswald",sans-serif;font-weight:500;font-size:14.8px;line-height:20px;color:var(--white);text-transform:uppercase;letter-spacing:0}
.feature-copy{position:absolute;left:26px;top:206px;width:478px;font-size:10px;line-height:13px;color:#e4ebf4}
.feature-copy p+p{margin-top:8px}
.rule{left:256px;top:414px;width:520px;height:5px;background:var(--blue)}
.contact-bar{left:130px;top:441px;width:646px;height:62px;background:var(--navy);border-radius:18px 0 0 0}
.contact-bar .row1{position:absolute;left:22px;top:6px;display:flex;align-items:center;gap:22px;color:var(--white)}
.contact-bar .email{font-size:19px}
.contact-bar .tel{font-family:"Lato",sans-serif;font-weight:700;font-size:22px}
.contact-bar .address{position:absolute;left:10px;top:36px;font-weight:700;font-size:13px;color:var(--white)}

/* back */
.quote-tab{left:0;top:10px;width:368px;height:64px;background:var(--blue);border-radius:0 0 30px 0}
.quote-tab p{position:absolute;left:14px;top:16px;width:320px;text-align:center;font-family:"Oswald",sans-serif;font-weight:500;font-size:13.5px;line-height:17px;color:var(--white);text-transform:uppercase}
.step{position:absolute;left:0;width:371px;display:flex;align-items:center;color:var(--white)}
.step.dark{background:var(--navy)}
.step.mid{background:var(--blue)}
.step .num{flex:0 0 56px;text-align:center;font-family:"Oswald",sans-serif;font-weight:700;font-size:66px;line-height:1}
.step .text{font-weight:700;font-size:9.5px;line-height:12.5px;padding-right:14px}
.step .text strong{font-size:12px}
.stamp{left:671px;top:42px;width:78px;height:78px;border:1.5px solid var(--ink)}
.address-line{left:511px;width:255px;height:1px;background:var(--line)}
.back .logo{left:511px;top:338px}
.back-contact{left:486px;top:423px;width:290px;height:60px;background:var(--blue);border-radius:26px 0 0 0;color:var(--white)}
.back-contact .tel{position:absolute;right:12px;top:4px;font-family:"Lato",sans-serif;font-weight:700;font-size:22px;display:flex;align-items:center;gap:8px}
.back-contact .email{position:absolute;right:12px;top:34px;font-size:17px;display:flex;align-items:center;gap:4px}
.address-band{left:0;top:475px;width:776px;height:28px;background:var(--blue);color:var(--white);font-size:19.5px;padding-left:24px;line-height:28px;white-space:nowrap}
</style>
</head>
<body>

<section class="card front" aria-label="Postcard front">
  <svg class="abs top-swoosh" viewBox="0 0 776 160" aria-hidden="true">
    <path d="M0 100 Q300 170 520 110 L776 90 L776 160 L0 160Z" fill="#dfe6ee"/>
    <path d="M0 0 L776 0 L776 20 Q500 10 0 60Z" fill="#eef2f6"/>
  </svg>

  <div class="abs logo firm-mark">
    <span class="square"></span>
    <div>
      <div class="name">Milo T. Varnum, P.A.</div>
      <div class="sub">ATTORNEYS AT LAW</div>
    </div>
  </div>

  <div class="abs phone-tab primary">
    <svg class="icon" width="20" height="20" viewBox="0 0 20 20" aria-hidden="true"><rect width="20" height="20" rx="4" fill="#fff"/><path d="M6 4c1 0 2 2 2 3s-1 1-1 2 2 3 3 3 1-1 2-1 3 1 3 2-1 2-2 2C8 15 5 10 5 6c0-1 0-2 1-2z" fill="#1f6bb5"/></svg>
    <span>201.555.0147</span>
  </div>
  <div class="abs phone-tab secondary">
    <svg class="icon" width="20" height="20" viewBox="0 0 20 20" aria-hidden="true"><rect width="20" height="20" rx="4" fill="#fff"/><path d="M6 4c1 0 2 2 2 3s-1 1-1 2 2 3 3 3 1-1 2-1 3 1 3 2-1 2-2 2C8 15 5 10 5 6c0-1 0-2 1-2z" fill="#15294a"/></svg>
    <span>732-555-0192</span>
  </div>

  <div class="abs lead-panel"></div>
  <h1 class="abs headline">When it comes to collecting PIP benefits, everything matters!</h1>
  <div class="abs portrait" role="img" aria-label="Portrait photo of the attorney in a dark suit"></div>
  <p class="abs lead-copy">For over 10 years, Milo T. Varnum has devoted his practice to representing medical providers in pursuit of their money against auto insurance carriers.</p>

  <div class="abs feature-panel">
    <div class="frame crash" role="img" aria-label="Photo of a firefighter at a car crash"></div>
    <div class="frame surgery" role="img" aria-label="Photo of surgeons in an operating room"></div>
    <h2 class="feature-title">Milo has successfully recovered millions of dollars for his clients</h2>
    <div class="feature-copy">
      <p><strong>Milo T. Varnum, P.A.</strong> services a wide variety of healthcare clients, including multi-disciplinary practices, hospitals, ambulatory care facilities, diagnostic centers, physicians and physician groups, skilled or certified practitioners, corporations, medical billing and management companies and related entities.</p>
      <p>Our firm operates together with your existing infrastructure to smoothly transmit referrals, shorten revenue cycles, and maximize reimbursements while lowering active account receivables.</p>
    </div>
  </div>
  <div class="abs rule"></div>

  <div class="abs contact-bar">
    <div class="row1">
      <span class="email">
        <svg class="icon" width="16" height="16" viewBox="0 0 16 16" aria-hidden="true"><g fill="none" stroke="#fff" stroke-width="1.3"><circle cx="8" cy="8" r="7"/><ellipse cx="8" cy="8" rx="3" ry="7"/><path d="M1 8h14"/></g></svg>
        MILO@MILOVARNUM.COM</span>
      <span class="tel">
        <svg class="icon" width="18" height="18" viewBox="0 0 20 20" aria-hidden="true"><rect width="20" height="20" rx="4" fill="#fff"/><path d="M6 4c1 0 2 2 2 3s-1 1-1 2 2 3 3 3 1-1 2-1 3 1 3 2-1 2-2 2C8 15 5 10 5 6c0-1 0-2 1-2z" fill="#15294a"/></svg>
        201.555.0147</span>
    </div>
    <div class="address">Harbor Point Offices. 44 Broad Street. 3rd Floor. Red Bank. NJ. 07701</div>
  </div>
</section>

<section class="card back" aria-label="Postcard back">
  <div class="abs quote-tab">
    <p>"If you represent healthcare providers, you should know Milo T. Varnum, P.A."</p>
  </div>

  <div class="step dark" style="top:80px;height:83px"><span class="num">1</span><p class="text">Our firm combines knowledge, experience and technology enabling us to move your matter and faster recovery means everything!</p></div>
  <div class="step mid" style="top:170px;height:80px"><span class="num">2</span><p class="text">Our firm will represent you for the collection of overdue or denied PIP bills. When we prevail, you are entitled to be not only paid, but to be paid with interest. Our firm advances all filing fees. You will incur no expense or be obligated to pay any counsel fee.</p></div>
  <div class="step dark" style="top:257px;height:76px"><span class="num">3</span><p class="text"><strong>Milo T. Varnum, P.A.</strong> is committed to keeping our clients advised on the status of their matters throughout the arbitration process. Our technology will enable you to view the up-to-date status of your files via the internet 24/7.</p></div>
  <div class="step mid" style="top:340px;height:90px"><span class="num">4</span><p class="text">We have well-trained lawyers and staff capable of assisting you at any juncture and we would welcome the opportunity to meet with your company so that you may learn more and allow us to show you why medical providers all over the New Jersey choose <strong>Milo T. Varnum, P.A.</strong> as their advocate in PIP arbitration.</p></div>

  <div class="abs stamp"></div>
  <div class="abs address-line" style="top:155px"></div>
  <div class="abs address-line" style="top:191px"></div>
  <div class="abs address-line" style="top:228px"></div>

  <div class="abs logo firm-mark">
    <span class="square" style="width:40px;height:40px"></span>
    <div>
      <div class="name" style="font-size:21px">Milo T. Varnum, P.A.</div>
      <div class="sub" style="font-size:11px">ATTORNEYS AT LAW</div>
    </div>
  </div>

  <div class="abs back-contact">
    <div class="tel">
      <svg class="icon" width="20" height="20" viewBox="0 0 20 20" aria-hidden="true"><rect width="20" height="20" rx="4" fill="#fff"/><path d="M6 4c1 0 2 2 2 3s-1 1-1 2 2 3 3 3 1-1 2-1 3 1 3 2-1 2-2 2C8 15 5 10 5 6c0-1 0-2 1-2z" fill="#1f6bb5"/></svg>
      201.555.0147</div>
    <div class="email">
      <svg class="icon" width="16" height="16" viewBox="0 0 16 16" aria-hidden="true"><g fill="none" stroke="#fff" stroke-width="1.3"><circle cx="8" cy="8" r="7"/><ellipse cx="8" cy="8" rx="3" ry="7"/><path d="M1 8h14"/></g></svg>
      MILO@MILOVARNUM.COM</div>
  </div>

  <div class="abs address-band">Harbor Point Offices. 44 Broad Street. 3rd Floor. Red Bank. NJ.</div>
</section>

</body>
</html>
```